Join Our Real Estate Team

I would like to purchase a customized version of a design you have previously submitted - https://www.artpitchly.com/design/61937402

I want to create a recruitment AD. I have attached a AD I have created and would like as much of this information on an AD as possible. My main GOAL is to promote $350 Flat Fee (Includes E&O) per Transaction & No Monthly Fees.
I like to use a photo stock as I have in the attachment of various people.
I DON'T want to say "Wanted". Prefer to say something like "STOP Paying High Splits...Keep Most of YOUR hard earned Commissions"
Feel free to use other formats that might fit all the information that I have in my flyer I have uploaded.

Target Market(s)

Realtors

Industry/Entity Type

Real Estate

Font styles to use
Serif

Colors
0094D4
00A9DD
6FCCEA
C7EBF8
E9F6FB

Requirements
Must have
• See uploaded flyer to get must haves
Nice to have
• See uploaded flyer to get ideas
Should not have
• Do not want it to say "wanted"

```html
<!DOCTYPE html>
<html lang="en">
<head>
<meta charset="utf-8">
<title>Join Our Real Estate Team</title>
<link rel="stylesheet" href="https://fonts.googleapis.com/css2?family=Montserrat:wght@500;600;700;800&display=swap">
<style>
  :root {
    --blue: #00a9dd;
    --blue-deep: #0094d4;
    --blue-soft: #6fccea;
    --ice: #e9f6fb;
    --ink: #0b2a21;
    --paper: #ffffff;
    --mist: #f4f4f4;
    --rule: #2c2c2c;
    --sweater: #8fa6c4;
    --shirt: #f3f3f1;
    --blouse: #e9bcc0;
    --skin: #c9a088;
  }
  * { box-sizing: border-box; margin: 0; padding: 0; }
  html, body { width: 1200px; height: 1200px; overflow: hidden; background: var(--paper); }
  body { font-family: "Montserrat", Arial, sans-serif; color: var(--ink); }
  .ad { position: relative; width: 1200px; height: 1200px; background: var(--paper); overflow: hidden; }

  .team-photo {
    position: absolute; left: 0; top: 0; width: 1200px; height: 611px;
    background:
      linear-gradient(180deg, rgba(250,250,248,0.95) 0%, rgba(240,238,234,0.55) 22%, rgba(220,200,185,0.15) 45%, rgba(255,255,255,0) 60%),
      linear-gradient(90deg, var(--sweater) 0%, #9fb0c8 16%, #d9c2b2 26%, var(--shirt) 38%, #f7f7f5 52%, #e6e9f0 66%, #d8c6c3 76%, var(--blouse) 86%, #e5b3b8 100%);
  }
  .team-photo::after {
    content: ""; position: absolute; inset: 0;
    background: radial-gradient(ellipse 70% 40% at 50% 30%, rgba(201,160,136,0.28), rgba(201,160,136,0) 70%);
  }
  .brand {
    position: absolute; left: 430px; top: 408px; width: 336px; height: 203px;
    background: var(--paper); display: flex; flex-direction: column;
    align-items: center; justify-content: center; gap: 12px;
  }
  .brand-mark { width: 46px; height: 46px; background: var(--blue-soft); }
  .brand-name { font-weight: 700; font-size: 24px; color: var(--ink); text-align: center; line-height: 1.25; }

  .headline { position: absolute; left: 0; width: 1200px; text-align: center; font-weight: 700; }
  .headline-main { top: 628px; font-size: 60px; color: var(--blue); letter-spacing: 0.6px; }
  .headline-sub { top: 702px; font-size: 46px; color: var(--ink); }

  .offer {
    position: absolute; left: 52px; top: 783px; width: 1094px; height: 124px;
    border: 2px solid var(--blue-deep); border-radius: 12px; overflow: hidden; display: flex;
  }
  .offer-example { position: relative; width: 570px; padding: 15px 0 0 68px; }
  .offer-pitch {
    position: relative; flex: 1; background: var(--blue); color: var(--paper);
    padding: 15px 0 0 94px; border-radius: 12px 0 0 12px;
  }
  .arrow { position: absolute; left: 10px; top: 34px; width: 22px; height: 58px; }
  .offer-pitch .arrow { left: 6px; }
  .example-line { font-size: 23px; font-weight: 600; line-height: 1.2; }
  .example-fee { font-size: 31px; font-weight: 700; color: var(--blue); line-height: 1.15; }
  .pitch-lead { font-size: 23px; font-weight: 600; line-height: 1.3; }
  .pitch-main { font-size: 26px; font-weight: 700; line-height: 1.25; }

  .contact-band { position: absolute; left: 0; top: 930px; width: 1200px; height: 195px; background: var(--mist); }
  .contact { position: absolute; left: 52px; top: 22px; }
  .contact-name { margin-left: 46px; font-size: 25px; font-weight: 700; color: var(--blue); }
  .contact-row { display: flex; align-items: center; gap: 22px; }
  .contact-row svg { width: 24px; height: 24px; flex: none; }
  .contact-phone { font-size: 38px; font-weight: 800; line-height: 1.05; }
  .contact-text { font-size: 25px; font-weight: 500; }
  .contact-text .accent { color: var(--blue); }
  .divider { position: absolute; left: 609px; top: 30px; width: 1.5px; height: 142px; background: var(--rule); }
  .question { position: absolute; left: 647px; top: 40px; font-size: 34px; font-weight: 700; color: var(--blue); line-height: 1.22; }

  .footer { position: absolute; left: 0; top: 1125px; width: 1200px; height: 75px; background: var(--ink); }
  .footer-cta {
    position: absolute; left: 0; top: 0; width: 672px; height: 75px; background: var(--blue);
    clip-path: polygon(0 0, 100% 0, 95% 100%, 0 100%);
    color: var(--paper); font-size: 27px; font-weight: 700; padding: 20px 0 0 48px;
  }
  .footer-tag { position: absolute; left: 690px; top: 23px; width: 470px; text-align: center; font-size: 26px; font-weight: 700; color: var(--blue); }
</style>
</head>
<body>
<main class="ad">
  <div class="team-photo" role="img" aria-label="Stock photo of a smiling, diverse group of seven real estate professionals standing together in a bright office"></div>

  <div class="brand">
    <span class="brand-mark"></span>
    <span class="brand-name">Coastal Keys<br>Realty Group, LLC</span>
  </div>

  <h1 class="headline headline-main">$350 FLAT FEE (INCLUDES E&amp;O)</h1>
  <p class="headline headline-sub">PER TRANSACTION &amp; NO MONTHLY FEES.</p>

  <section class="offer">
    <div class="offer-example">
      <svg class="arrow" viewBox="0 0 22 58"><polygon points="0,0 22,29 0,58" fill="var(--blue)"/></svg>
      <p class="example-line">On a $250,000 Sale w/3% Commission</p>
      <p class="example-fee">$350* FLAT FEE = $ 7,150</p>
      <p class="example-line">Commission Earned w/CKRG</p>
    </div>
    <div class="offer-pitch">
      <svg class="arrow" viewBox="0 0 22 58"><polygon points="0,0 22,29 0,58" fill="var(--paper)"/></svg>
      <p class="pitch-lead">Stop Paying High Splits....</p>
      <p class="pitch-main">KEEP MOST OF YOUR HARD<br>EARNED COMMISSIONS</p>
    </div>
  </section>

  <section class="contact-band">
    <div class="contact">
      <p class="contact-name">DANA MORROW</p>
      <div class="contact-row">
        <svg viewBox="0 0 24 24"><circle cx="12" cy="12" r="12" fill="var(--blue)"/><path d="M8.2 6.5l2 2.2-1 1.4c.8 1.8 2 3 3.8 3.8l1.4-1 2.2 2-1.3 1.8c-4.4-.4-8.4-4.4-8.8-8.8z" fill="var(--paper)"/></svg>
        <span class="contact-phone">555.014.2280</span>
      </div>
      <div class="contact-row" style="margin-top:14px">
        <svg viewBox="0 0 24 24"><circle cx="12" cy="12" r="12" fill="var(--blue)"/><rect x="6" y="8" width="12" height="8.5" rx="1" fill="none" stroke="var(--paper)" stroke-width="1.5"/><path d="M6.5 8.5l5.5 4 5.5-4" fill="none" stroke="var(--paper)" stroke-width="1.5"/></svg>
        <span class="contact-text">Dana@CoastalKeysRG.com</span>
      </div>
      <div class="contact-row" style="margin-top:6px">
        <svg viewBox="0 0 24 24"><circle cx="12" cy="12" r="12" fill="var(--blue)"/><g fill="none" stroke="var(--paper)" stroke-width="1.3"><circle cx="12" cy="12" r="6"/><ellipse cx="12" cy="12" rx="2.6" ry="6"/><path d="M6 12h12"/></g></svg>
        <span class="contact-text">www.<span class="accent">CoastalKeysRealtyGroup</span>.com</span>
      </div>
    </div>
    <div class="divider"></div>
    <p class="question">ARE YOU FRUSTRATED<br>GIVING UP 20%, 30% or Even<br>50% of your Commission???</p>
  </section>

  <footer class="footer">
    <div class="footer-cta">Join Our Team Start Earning More Today!</div>
    <div class="footer-tag">YOUR PHENOMENAL BROKER</div>
  </footer>
</main>
</body>
</html>
```